Stationary for Corwin Lattimore | ||
Business card, letterhead, with compliments slip, envelope | ||
Use same font as used in my logo | ||
Corporate Traditional Professional Simple |
[firstname] [surname] | ||
[title] | ||
1 Some Street Sometown Somewhereshire SW23 8SW |
someone@corwinlattimore.example | ||
www.corwinlattimore.example | ||
I am the sole employee at the moment. In the future, I hope to have other employees, so I will add a 'title' section later. Please bear this in mind when positioning the information. I am looking for something that is elegant, professional, minimilistic and tasteful. Please take a look at the website: http://www.corwinlattimore.example using the following credentials to log in: u/n: "pinewhisk" p/w: "pinewhisk847" Please feel free to message me for more information. Most importantly, I want the logo and other key information (like my name?) to be in silver (PMS 877 Metallic). |
I am flexible on this. I want space on my business cards for people to be able to write some information on. | ||

```html
<!DOCTYPE html>
<html lang="en">
<head>
<meta charset="utf-8">
<title>Corwin Lattimore – Business Cards</title>
<link href="https://fonts.googleapis.com/css2?family=Cormorant+SC:wght@400;500&display=swap" rel="stylesheet">
<style>
  :root {
    --backdrop: #000000;
    --silver-light: #f4f4f4;
    --silver-mid: #d4d4d4;
    --silver: #8e8e8e;
    --slate: #9b9b9b;
    --ink: #7a7a7a;
    --ink-soft: #9a9a9a;
    --paper: #ffffff;
  }
  * { margin: 0; padding: 0; box-sizing: border-box; }
  html, body { width: 1200px; height: 850px; overflow: hidden; background: var(--backdrop); }
  body { position: relative; font-family: "Cormorant SC", "Times New Roman", serif; }

  .card { position: absolute; border-radius: 9px; overflow: hidden; }

  .card--front { top: 113px; height: 300px; }
  .card--front-silver {
    left: 65px; width: 530px;
    background: linear-gradient(160deg, var(--paper) 0%, var(--silver-light) 40%, var(--silver-mid) 100%);
  }
  .card--front-slate {
    left: 605px; width: 535px;
    background: linear-gradient(160deg, #a6a6a6 0%, var(--slate) 60%, #8f8f8f 100%);
  }
  .card--back { top: 432px; height: 336px; background: var(--paper); }
  .card--back-left { left: 65px; width: 530px; }
  .card--back-right { left: 605px; width: 535px; }

  .brand {
    position: absolute; left: 50%; top: 112px; transform: translateX(-50%);
    display: flex; align-items: center; gap: 12px;
    color: var(--silver); font-weight: 500; white-space: nowrap;
  }
  .card--front-slate .brand { color: var(--paper); }
  .brand__mark { width: 34px; height: 34px; background: currentColor; }
  .brand__name { font-size: 32px; line-height: 0.95; letter-spacing: 0.5px; }

  .web {
    position: absolute; left: 0; right: 0; top: 246px; text-align: center;
    font-size: 9px; letter-spacing: 1px; color: var(--silver);
  }
  .card--front-slate .web { color: var(--paper); }

  .holder { position: absolute; left: 28px; top: 38px; color: var(--ink); }
  .holder__name { font-size: 28px; font-weight: 500; letter-spacing: 1px; line-height: 1; }
  .holder__title { font-size: 12px; letter-spacing: 1.2px; margin-top: 6px; }

  .contact {
    position: absolute; left: 30px; top: 190px;
    font-size: 10px; line-height: 14px; color: var(--ink-soft); letter-spacing: 0.4px;
    border-collapse: collapse; white-space: nowrap;
  }
  .contact td { vertical-align: top; padding: 0; }
  .contact .contact__label { padding-left: 16px; position: relative; width: 82px; }
  .contact .contact__label::before {
    content: ""; position: absolute; left: 0; top: 5px; width: 4px; height: 4px; background: var(--ink-soft);
  }
  .contact .contact__gap td { height: 14px; }

  .statue {
    position: absolute; right: 0; top: 40px; width: 150px; height: 220px;
    background: linear-gradient(180deg, #cfcfcf 0%, #a8a8a8 55%, #8f8f8f 100%);
    border-top-left-radius: 70px;
  }
</style>
</head>
<body>

  <section class="card card--front card--front-silver">
    <div class="brand">
      <span class="brand__mark"></span>
      <span class="brand__name">Corwin<br>Lattimore</span>
    </div>
    <p class="web">www.corwinlattimore.example</p>
  </section>

  <section class="card card--front card--front-slate">
    <div class="brand">
      <span class="brand__mark"></span>
      <span class="brand__name">Corwin<br>Lattimore</span>
    </div>
    <p class="web">www.corwinlattimore.example</p>
  </section>

  <section class="card card--back card--back-left">
    <div class="holder">
      <h1 class="holder__name">Alden Marsh</h1>
      <p class="holder__title">Architect / President</p>
    </div>
    <table class="contact">
      <tr><td class="contact__label">Address</td><td>: &nbsp;12 Harrow Lane, Eastmere</td></tr>
      <tr><td></td><td>&nbsp;&nbsp;&nbsp;Northwoldshire, NW14 3QT</td></tr>
      <tr class="contact__gap"><td></td><td></td></tr>
      <tr><td class="contact__label">Phone</td><td>: &nbsp;+44 (0)1632 960418</td></tr>
      <tr><td class="contact__label">Mobile</td><td>: &nbsp;+44 (0)7700 900214</td></tr>
      <tr><td class="contact__label">Email</td><td>: &nbsp;someone@corwinlattimore.example</td></tr>
    </table>
    <div class="statue" role="img" aria-label="Silver classical seated statue illustration"></div>
  </section>

  <section class="card card--back card--back-right">
    <div class="holder">
      <h1 class="holder__name">Alden Marsh</h1>
      <p class="holder__title">Architect / President</p>
    </div>
    <table class="contact">
      <tr><td class="contact__label">Address</td><td>: &nbsp;12 Harrow Lane, Eastmere</td></tr>
      <tr><td></td><td>&nbsp;&nbsp;&nbsp;Northwoldshire, NW14 3QT</td></tr>
      <tr class="contact__gap"><td></td><td></td></tr>
      <tr><td class="contact__label">Phone</td><td>: &nbsp;+44 (0)1632 960418</td></tr>
      <tr><td class="contact__label">Mobile</td><td>: &nbsp;+44 (0)7700 900214</td></tr>
      <tr><td class="contact__label">Email</td><td>: &nbsp;someone@corwinlattimore.example</td></tr>
    </table>
    <div class="statue" role="img" aria-label="Silver classical seated statue illustration"></div>
  </section>

</body>
</html>
```